A4 Informational Flyer - Summer Pathology Course

We are looking to deliver a QRV27350 Certificate IV in Pathology Summer Course Specifically aimed at current University/TAFE students studying in a health related qualification e.g. Nursing students, Medical students, Pathology students etc.

The basis around it is that our potential students will complete this shortened summer course over the Christmas, new year break 2014/2015 which will enable them to gain further skills in the health related area and they will then be able to work in the pathology field whilst still studying - instead of working a side job at Brindleton's to support them.

We would like to use slogans on the flyer for engagement such as "Sick of flipping burgers?" "Are you looking to gain additional skills in a health related field" etc. anything you can come up with as the designer, is also welcomed.

Designer to include information regarding the course as follows:

Course Introduction:

This is a National Training Package and is designed to train people wishing to pursue a career in the Pathology Collection Industry.
The modules within QRV27350 Certificate IV in Pathology provide the participants with training and skills development in a range of areas including Customer Service, Pathology Collection and Techniques, Phlebotomy (blood collection), Infection Control, Occupational Health and Safety and knowledge of the disease processes associated with clients of all ages who may require Pathology Collection.

Government Funding is available for eligible students.

Fees:

Government Funded Student Fees:
Tuition: $425
If you also have a healthcare card, $85
Resources: $355

Fee For Service Student Fees:
Tuition: $2,365
Resources: $355

Method of Study:

The summer QRV27350 Certificate IV in Pathology program is run on campus at both our Kestrelford and Ambleton training facilities. Students will attend classes two (2) days per week from 9.30am to 2.30pm. Some workbooks are required to be completed off-campus. Extensive practical experience is undertaken in the Vexmoor Learning Hub clinical laboratories.

Course Commencement & Duration:

Course will commence late November 2014 and includes one (1) fast track week and one (1) 4 day week. Classes will conclude by the late January 2015. (Includes 2 week break over Christmas/New Year). *Subject to student numbers

Application Process:

Complete an online enrollment form via our website www.vexmoorlearninghub.edu.au and our student administration will contact you within 24 hours to discuss your enrollment and the next steps to secure your place on the course.
Alternatively, contact one of our friendly staff members on 03 7215 6048 for further assistance and information.

Please include our attached logos, photos for engagement etc where appropriate.
Please include our website in bold: www.vexmoorlearninghub.edu.au and our phone number is bold 03 7215 6048

Please also include our "TOID No. 31785" under our logo.

We would like this overall flyer/brochure to be engaging, bold, simply, easy to read for potential students. Keeping with our company colors as much as possible is a must.

Formats must be in a normal format such as PDF for printing purposes and also a JPEG, ESP format so we can use to advertise as a picture on Pinwheelia etc.

Industry/Entity Type

Healthcare

Font styles to use
Serif

Colors
f37123
ffc214
faa54b

Requirements
Must have
• A4, 1 sided please.

Must include codes next to course title.

```html
<!DOCTYPE html>
<html lang="en">
<head>
<meta charset="utf-8">
<title>Vexmoor Learning Hub – Summer Pathology Course</title>
<link href="https://fonts.googleapis.com/css2?family=Lora:ital,wght@0,400;0,700;1,700&display=swap" rel="stylesheet">
<style>
  :root {
    --orange: #f37123;
    --yellow: #ffc214;
    --peach: #faa54b;
    --white: #ffffff;
    --ink: #2a2622;
    --grey: #6d6e70;
  }
  * { box-sizing: border-box; margin: 0; padding: 0; }
  html, body { width: 848px; height: 1200px; overflow: hidden; }
  body { font-family: "Lora", Georgia, serif; color: var(--ink); }

  .flyer {
    position: relative;
    width: 848px;
    height: 1200px;
    overflow: hidden;
    background: linear-gradient(180deg, #fec94a 0%, var(--peach) 45%, var(--orange) 85%);
  }

  .headline {
    position: absolute;
    right: 36px;
    top: 50px;
    width: 440px;
    text-align: right;
    font-weight: 700;
    font-style: italic;
    font-size: 37px;
    line-height: 1.18;
    color: var(--white);
    text-shadow: 2px 3px 4px rgba(150, 70, 0, .45);
  }

  .photo {
    position: absolute;
    border-radius: 50%;
    border: 6px solid var(--white);
    box-shadow: 0 3px 10px rgba(120, 60, 0, .3);
  }
  .photo--trainer {
    left: 34px; top: 14px; width: 356px; height: 356px;
    background: radial-gradient(circle at 40% 45%, #f3eee8 0%, #d9c4b4 45%, #b14a3c 75%, #e7ddd4 100%);
  }
  .photo--collection {
    left: 440px; top: 252px; width: 214px; height: 214px;
    background: radial-gradient(circle at 45% 55%, #e9e4e0 0%, #6b5a6e 50%, #2c2630 80%, #d8d3d0 100%);
  }
  .photo--samples {
    left: 600px; top: 505px; width: 214px; height: 214px;
    background: radial-gradient(circle at 50% 50%, #f4f2ee 0%, #e2a35a 40%, #cfd6dc 70%, #f0eeea 100%);
  }

  .section-title {
    position: absolute;
    left: 0;
    height: 28px;
    padding-left: 32px;
    font-weight: 700;
    font-size: 20px;
    line-height: 28px;
    color: var(--ink);
    background: linear-gradient(90deg, rgba(255,255,255,.95) 0%, rgba(255,255,255,.85) 55%, rgba(255,255,255,0) 100%);
  }
  .section-body {
    position: absolute;
    left: 34px;
    font-size: 12px;
    line-height: 16px;
    color: var(--ink);
  }
  .section-body p { text-align: justify; }

  .intro-title { top: 420px; width: 330px; }
  .intro-body { top: 452px; width: 452px; }

  .funding-title { top: 598px; width: 600px; font-size: 21px; }
  .fees { top: 634px; width: 640px; display: flex; gap: 40px; }
  .fees .col { width: 300px; }
  .fees h3 { font-size: 12px; font-weight: 700; font-style: italic; }
  .fees p { text-align: left; }
  .fees strong { font-weight: 700; }

  .method-title { top: 708px; width: 300px; }
  .method-body { top: 742px; width: 782px; }

  .dates-title { top: 810px; width: 420px; }
  .dates-body { top: 846px; width: 782px; }

  .apply-title { top: 904px; width: 300px; }
  .apply-body { top: 938px; width: 782px; }

  .footer-wave { position: absolute; left: 0; bottom: 0; width: 848px; height: 190px; }

  .brand {
    position: absolute;
    left: 46px;
    top: 1060px;
    display: flex;
    align-items: center;
    gap: 14px;
  }
  .brand-dot {
    width: 64px; height: 64px; border-radius: 50%;
    background: var(--orange);
  }
  .brand-name {
    font-size: 34px;
    line-height: 1.05;
    color: var(--grey);
    width: 250px;
  }
  .toid {
    position: absolute;
    left: 130px;
    top: 1160px;
    font-size: 11px;
    color: var(--ink);
  }

  .contact {
    position: absolute;
    right: 34px;
    top: 1106px;
    display: flex;
    flex-direction: column;
    align-items: flex-end;
    gap: 14px;
    font-weight: 700;
    font-size: 14px;
    color: var(--ink);
  }
  .contact-row { display: flex; align-items: center; gap: 8px; }
  .contact-icon { width: 24px; height: 24px; }
</style>
</head>
<body>
<main class="flyer">
  <div class="photo photo--trainer" role="img" aria-label="Photo of a trainer pointing at an anatomical torso model"></div>
  <div class="photo photo--collection" role="img" aria-label="Photo of a student taking a blood sample from an arm"></div>
  <div class="photo photo--samples" role="img" aria-label="Photo of a rack of blood collection tubes"></div>

  <h1 class="headline">Stop flippin’ and start earning like a health professional.</h1>

  <h2 class="section-title intro-title">Course Introduction:</h2>
  <div class="section-body intro-body">
    <p>This is a National Training Package and is designed to train people wishing to pursue a career in the Pathology Collection Industry.</p>
    <p>The modules within QRV27350 Certificate IV in Pathology provide the participants with training and skills development in a range of areas including Customer Service, Pathology Collection and Techniques, Phlebotomy (blood collection), Infection Control, Occupational Health and Safety and knowledge of the disease processes associated with clients of all ages who may require Pathology Collection.</p>
  </div>

  <h2 class="section-title funding-title">Government Funding is available for eligible students.</h2>
  <div class="section-body fees">
    <div class="col">
      <h3>Government Funded Student Fees:</h3>
      <p>Tuition: <strong>$425</strong></p>
      <p>If you also have a healthcare card, <strong>$85</strong></p>
      <p>Resources: <strong>$355</strong></p>
    </div>
    <div class="col">
      <h3>Fee For Service Student Fees:</h3>
      <p>Tuition: <strong>$2,365</strong></p>
      <p>Resources: <strong>$355</strong></p>
    </div>
  </div>

  <h2 class="section-title method-title">Method of Study:</h2>
  <div class="section-body method-body">
    <p>The summer QRV27350 Certificate IV in Pathology program is run on campus at both our Kestrelford and Ambleton training facilities. Students will attend classes two (2) days per week from 9.30am to 2.30pm. Some workbooks are required to be completed off-campus. Extensive practical experience is undertaken in the Vexmoor Learning Hub clinical laboratories.</p>
  </div>

  <h2 class="section-title dates-title">Course Commencement &amp; Duration:</h2>
  <div class="section-body dates-body">
    <p>Course will commence late November 2014 and includes one (1) fast track week and one (1) 4 day week. Classes will conclude by the late January 2015. (Includes 2 week break over Christmas/New Year). <strong><em>*Subject to student numbers</em></strong></p>
  </div>

  <h2 class="section-title apply-title">Application Process:</h2>
  <div class="section-body apply-body">
    <p style="text-align:left">Complete an online enrollment form via our website www.vexmoorlearninghub.edu.au and our student administration will contact you within 24 hours to discuss your enrollment and the next steps to secure your place on the course.<br>Alternatively, contact one of our friendly staff members on 03 7215 6048 for further assistance and information.</p>
  </div>

  <svg class="footer-wave" viewBox="0 0 848 190" preserveAspectRatio="none" aria-hidden="true">
    <path d="M0 40 C 200 -10, 420 70, 600 40 C 720 20, 800 10, 848 14 L 848 190 L 0 190 Z" fill="#ffffff"/>
  </svg>

  <div class="brand">
    <span class="brand-dot"></span>
    <span class="brand-name">Vexmoor Learning Hub</span>
  </div>
  <p class="toid">TOID No. 31785</p>

  <div class="contact">
    <div class="contact-row">
      <span>www.vexmoorlearninghub.edu.au</span>
      <svg class="contact-icon" viewBox="0 0 24 24" aria-hidden="true">
        <circle cx="12" cy="12" r="12" fill="#f37123"/>
        <circle cx="10.5" cy="10.5" r="4.5" fill="none" stroke="#fff" stroke-width="2"/>
        <line x1="14" y1="14" x2="18" y2="18" stroke="#fff" stroke-width="2.4" stroke-linecap="round"/>
      </svg>
    </div>
    <div class="contact-row">
      <span>03 7215 6048</span>
      <svg class="contact-icon" viewBox="0 0 24 24" aria-hidden="true">
        <circle cx="12" cy="12" r="12" fill="#f37123"/>
        <path d="M8.2 6.2 L10.2 6 L11.2 8.8 L9.8 9.9 C10.5 11.6 12.2 13.4 14 14.2 L15.1 12.8 L17.9 13.8 L17.7 15.8 C17.5 16.8 16.6 17.4 15.6 17.2 C10.9 16.3 7.7 13.1 6.8 8.4 C6.6 7.4 7.2 6.4 8.2 6.2 Z" fill="#fff"/>
      </svg>
    </div>
  </div>
</main>
</body>
</html>
```